Keystone Prime Water Tank

I primarily market the water tanks so want a business care that reflects that. I have attached the water tank logo. You have been working on our water tank so maybe we can use that on the card et. I am leaving as one sided but can be double sided if that works. The information that needs to be on the cards is as follows: Gerald T. Munro Phone numbers: Office 555-284-9137 Direct 555-619-2405 Mobile 555-372-5841 email address: gerald@fieldgearworks.com Address P.O. Box 8273 Windermere, FL 30512 Web Page: www.fieldgearworks.com. A lot to fit on the card. Thanks

```html
<!DOCTYPE html>
<html lang="en">
<head>
<meta charset="utf-8">
<title>Keystone Prime Water Tank – Business Card</title>
<link href="https://fonts.googleapis.com/css2?family=Archivo+Black&family=Archivo:wght@700;800&display=swap" rel="stylesheet">
<style>
  :root {
    --red: #ee1c1c;
    --blush: #f9c9c9;
    --blush-soft: #fbdcdc;
    --ink: #111111;
    --paper: #fdfdfd;
    --backdrop: #ffffff;
    --edge: #8a8a8a;
  }
  * { box-sizing: border-box; margin: 0; padding: 0; }
  html, body {
    width: 1200px; height: 1000px; overflow: hidden;
    background: var(--backdrop);
  }
  .canvas {
    position: relative; width: 1200px; height: 1000px;
    display: flex; flex-direction: column; align-items: center; justify-content: center;
    gap: 42px;
  }
  .card {
    position: relative; width: 700px; height: 453px;
    background: var(--paper);
    border: 1px solid var(--edge);
    box-shadow: 10px 14px 22px rgba(0,0,0,0.22);
    overflow: hidden;
  }

  /* Background pattern areas */
  .pattern-field { position: absolute; }
  .card-front .pattern-field {
    left: 320px; top: 30px; right: 0; bottom: 0;
    background: linear-gradient(150deg, rgba(249,201,201,0) 0%, rgba(249,201,201,0.55) 35%, var(--blush) 75%);
  }
  .card-back .pattern-field {
    left: 0; top: 0; width: 560px; bottom: 49px;
    background: linear-gradient(210deg, rgba(251,220,220,0) 0%, rgba(251,220,220,0.5) 45%, var(--blush-soft) 90%);
  }

  /* Front */
  .brand {
    position: absolute; left: 0; right: 0; top: 290px;
    display: flex; align-items: center; justify-content: center; gap: 12px;
  }
  .brand-mark { width: 26px; height: 26px; background: var(--red); }
  .brand-name {
    font-family: "Archivo Black", "Arial Black", sans-serif;
    font-size: 27px; color: var(--ink); letter-spacing: 0.3px; text-transform: uppercase;
  }

  /* Back */
  .holder-name {
    position: absolute; left: 0; right: 0; top: 100px; text-align: center;
    font-family: "Archivo Black", "Arial Black", sans-serif;
    font-size: 50px; color: var(--red); letter-spacing: 0.5px;
  }
  .contact-list {
    position: absolute; left: 114px; top: 252px; list-style: none;
    display: flex; flex-direction: column; gap: 17px;
  }
  .contact-item {
    display: flex; align-items: center; gap: 9px;
    font-family: "Archivo", Arial, sans-serif; font-weight: 800;
    font-size: 21px; color: var(--ink);
  }
  .contact-icon { width: 28px; height: 28px; flex: none; }
  .phone-band {
    position: absolute; left: 0; right: 0; bottom: 0; height: 49px;
    background: var(--red);
    display: flex; align-items: center; justify-content: center;
    font-family: "Archivo", Arial, sans-serif; font-weight: 800;
    font-size: 16.5px; color: #ffffff; letter-spacing: 0.2px;
  }
</style>
</head>
<body>
<main class="canvas">

  <section class="card card-front" aria-label="Card front">
    <div class="pattern-field" role="img" aria-label="Large faint pink brand pattern in the background"></div>
    <div class="brand">
      <span class="brand-mark"></span>
      <span class="brand-name">Keystone Prime Water Tank</span>
    </div>
  </section>

  <section class="card card-back" aria-label="Card back">
    <div class="pattern-field" role="img" aria-label="Faint pink brand pattern in the background"></div>
    <h1 class="holder-name">Gerald T. Munro</h1>

    <ul class="contact-list">
      <li class="contact-item">
        <svg class="contact-icon" viewBox="0 0 28 28" aria-hidden="true">
          <circle cx="14" cy="14" r="13" fill="var(--red)"/>
          <rect x="7.5" y="9.5" width="13" height="9" fill="none" stroke="#fff" stroke-width="1.6"/>
          <path d="M7.5 9.5 L14 15 L20.5 9.5" fill="none" stroke="#fff" stroke-width="1.6"/>
        </svg>
        gerald@fieldgearworks.com
      </li>
      <li class="contact-item">
        <svg class="contact-icon" viewBox="0 0 28 28" aria-hidden="true">
          <circle cx="14" cy="14" r="13" fill="var(--red)"/>
          <path d="M14 22 C10 17 8.5 14.5 8.5 12 A5.5 5.5 0 0 1 19.5 12 C19.5 14.5 18 17 14 22 Z" fill="#fff"/>
          <circle cx="14" cy="12" r="2.2" fill="var(--red)"/>
        </svg>
        P.O. Box 8273 Windermere, FL 30512
      </li>
      <li class="contact-item">
        <svg class="contact-icon" viewBox="0 0 28 28" aria-hidden="true">
          <circle cx="14" cy="14" r="13" fill="var(--red)"/>
          <g fill="none" stroke="#fff" stroke-width="1.4">
            <circle cx="14" cy="14" r="7"/>
            <ellipse cx="14" cy="14" rx="3" ry="7"/>
            <line x1="7" y1="14" x2="21" y2="14"/>
            <line x1="8.2" y1="10.5" x2="19.8" y2="10.5"/>
            <line x1="8.2" y1="17.5" x2="19.8" y2="17.5"/>
          </g>
        </svg>
        www.fieldgearworks.com
      </li>
    </ul>

    <div class="phone-band">Office 555-284-9137 /Direct 555-619-2405 /Mobile 555-372-5841</div>
  </section>

</main>
</body>
</html>
```